Coffeeshop menu for filter tip

We want to have a cannabis (coffeeshop) menu in the size 25mm wide x 60mm wide. Some examples attached.

it must have the following text:
Menu

WEED p/g
Vortigan €16
Tangerosa €14
Dusk Rover €14
Mangolina €16
Ultra Fern €14
Amber Hermit €14

HASH p/g
Nepali Bronze €12
Velvet Ember€11
Cedar Pine €14
Red Fable €10

Target Market(s)

tourist in Amsterdam

Requirements
Nice to have
• cannabis sign leaf
• No Cigarettes allowed symbol

```html
<!DOCTYPE html>
<html lang="en">
<head>
<meta charset="utf-8">
<title>Amsterdam Coffeeshop Menu</title>
<link rel="stylesheet" href="https://fonts.googleapis.com/css2?family=Kaushan+Script&family=Oswald:wght@700&family=Open+Sans:wght@400&display=swap">
<style>
  :root {
    --green-light: #0e713d;
    --green-dark: #08552c;
    --green-deep: #0b6134;
    --cream: #f1eed6;
    --rule: #d7dcc2;
    --text: #e4ead0;
    --yellow: #f5ef7c;
    --white: #ffffff;
    --leaf: #4fa83a;
    --red: #e3262c;
  }
  * { margin: 0; padding: 0; box-sizing: border-box; }
  html, body { width: 1200px; height: 2878px; overflow: hidden; }
  body {
    position: relative;
    background: radial-gradient(ellipse at 50% 40%, var(--green-light) 0%, var(--green-deep) 60%, var(--green-dark) 100%);
    font-family: "Open Sans", sans-serif;
    color: var(--text);
  }
  .frame { position: absolute; inset: 0; width: 1200px; height: 2878px; }

  .emblem {
    position: absolute; left: 409px; top: 108px;
    width: 380px; height: 380px; border-radius: 50%;
    background: var(--white);
    display: flex; align-items: center; justify-content: center;
  }
  .emblem-ring {
    width: 348px; height: 348px; border-radius: 50%;
    border: 8px solid var(--green-deep);
    display: flex; align-items: center; justify-content: center;
  }
  .emblem-leaf {
    width: 290px; height: 290px; border-radius: 50%;
    background: radial-gradient(circle, var(--leaf) 0%, rgba(79,168,58,0.35) 55%, rgba(255,255,255,0) 72%);
  }

  .city {
    position: absolute; left: 0; width: 1200px; top: 478px;
    text-align: center;
    font-family: "Kaushan Script", cursive;
    font-size: 94px; line-height: 1;
    color: var(--yellow);
  }
  .title {
    position: absolute; left: 0; width: 1200px; top: 570px;
    text-align: center;
    font-family: "Oswald", sans-serif; font-weight: 700;
    font-size: 214px; line-height: 1.0; letter-spacing: 2px;
    color: var(--white);
  }

  .section { position: absolute; left: 239px; width: 735px; }
  .section-weed { top: 830px; }
  .section-hash { top: 1850px; }
  .section-head { position: relative; height: 187px; }
  .section-name {
    position: absolute; left: -4px; bottom: 4px;
    font-family: "Kaushan Script", cursive;
    font-size: 150px; line-height: 1;
    color: var(--yellow);
  }
  .unit {
    position: absolute; left: 593px; bottom: 22px;
    font-size: 66px; line-height: 1; color: var(--text);
  }
  .section-hash .section-head { height: 216px; }
  .section-hash .unit { bottom: 48px; }

  .items { list-style: none; }
  .item {
    position: relative;
    height: 126.4px;
    display: flex; align-items: flex-end;
    padding: 0 0 20px 18px;
    font-size: 68px; line-height: 1;
    border-bottom: 2px solid var(--rule);
  }
  .item::before, .item::after {
    content: ""; position: absolute; bottom: -4px;
    width: 6px; height: 6px; border-radius: 50%; background: var(--rule);
  }
  .item::before { left: -2px; }
  .item::after { right: -2px; }
  .item-name { flex: 1; color: var(--text); }
  .item-price { width: 138px; color: var(--yellow); }
  .section-weed .item:first-child { height: 100px; }
  .section-hash .item:first-child { height: 100px; }

  .notice {
    position: absolute; left: 346px; top: 2655px;
    display: flex; align-items: center; gap: 20px;
    font-size: 48px; line-height: 1; color: var(--white);
  }
  .notice svg { width: 102px; height: 102px; }
</style>
</head>
<body>
  <svg class="frame" viewBox="0 0 1200 2878" aria-hidden="true">
    <path d="M78 43 L1123 43 A40 40 0 0 0 1163 83 L1163 2797 A40 40 0 0 0 1123 2837 L78 2837 A40 40 0 0 0 38 2797 L38 83 A40 40 0 0 0 78 43 Z"
          fill="none" stroke="var(--cream)" stroke-width="5"/>
    <path d="M86 59 L1115 59 A32 32 0 0 0 1147 91 L1147 2789 A32 32 0 0 0 1115 2821 L86 2821 A32 32 0 0 0 54 2789 L54 91 A32 32 0 0 0 86 59 Z"
          fill="none" stroke="var(--cream)" stroke-width="2.5"/>
  </svg>

  <div class="emblem">
    <div class="emblem-ring">
      <div class="emblem-leaf" role="img" aria-label="Green cannabis leaf illustration"></div>
    </div>
  </div>

  <div class="city">Amsterdam</div>
  <h1 class="title">MENU</h1>

  <section class="section section-weed">
    <div class="section-head">
      <h2 class="section-name">Weed</h2>
      <span class="unit">p/g</span>
    </div>
    <ul class="items">
      <li class="item"><span class="item-name">Vortigan</span><span class="item-price">€16</span></li>
      <li class="item"><span class="item-name">Tangerosa</span><span class="item-price">€14</span></li>
      <li class="item"><span class="item-name">Dusk Rover</span><span class="item-price">€14</span></li>
      <li class="item"><span class="item-name">Mangolina</span><span class="item-price">€16</span></li>
      <li class="item"><span class="item-name">Ultra Fern</span><span class="item-price">€14</span></li>
      <li class="item"><span class="item-name">Amber Hermit</span><span class="item-price">€14</span></li>
    </ul>
  </section>

  <section class="section section-hash">
    <div class="section-head">
      <h2 class="section-name">Hash</h2>
      <span class="unit">p/g</span>
    </div>
    <ul class="items">
      <li class="item"><span class="item-name">Nepali Bronze</span><span class="item-price">€12</span></li>
      <li class="item"><span class="item-name">Velvet Ember</span><span class="item-price">€11</span></li>
      <li class="item"><span class="item-name">Cedar Pine</span><span class="item-price">€14</span></li>
      <li class="item"><span class="item-name">Red Fable</span><span class="item-price">€10</span></li>
    </ul>
  </section>

  <div class="notice">
    <svg viewBox="0 0 100 100" aria-hidden="true">
      <circle cx="50" cy="50" r="46" fill="var(--white)"/>
      <rect x="18" y="54" width="56" height="10" fill="var(--green-deep)"/>
      <rect x="74" y="54" width="10" height="10" fill="var(--green-deep)"/>
      <path d="M30 48 C30 38 40 40 38 30" fill="none" stroke="var(--green-deep)" stroke-width="3"/>
      <circle cx="50" cy="50" r="42" fill="none" stroke="var(--red)" stroke-width="9"/>
      <line x1="21" y1="21" x2="79" y2="79" stroke="var(--red)" stroke-width="9"/>
    </svg>
    <span class="notice-text">NO CIGARETTES</span>
  </div>
</body>
</html>
```